ashby paving works

Needs to have phone number 0412885107 and email marklowry@pavemail.com.au.
ABN 27613048852
name mark lowry

For all your concreting solutions
Excavation
Exposed & colour concrete
House & shed slabs
Driveways
Landing & steps

Contact Information for Business Card

ph 0412885107
email marklowry@pavemail.com.au.
ABN 27613048852
name mark lowry

```html
<!DOCTYPE html>
<html lang="en">
<head>
<meta charset="utf-8">
<title>Ashby Paving Works – Business Card</title>
<link href="https://fonts.googleapis.com/css2?family=Rajdhani:wght@500;600;700&display=swap" rel="stylesheet">
<style>
  :root {
    --orange: #e8672f;
    --charcoal: #5b5350;
    --paper: #ffffff;
    --backdrop: #eceeed;
    --rule: #6a625f;
  }
  * { margin: 0; padding: 0; box-sizing: border-box; }
  html, body {
    width: 848px; height: 1200px; overflow: hidden;
    background: var(--backdrop);
    font-family: "Rajdhani", "Arial Narrow", sans-serif;
  }
  .card {
    position: absolute; left: 114px; width: 620px; height: 369px;
    background: var(--paper);
    box-shadow: 0 6px 18px rgba(0,0,0,0.12);
    overflow: hidden;
  }
  .card--front { top: 150px; }
  .card--back { top: 640px; }

  /* front */
  .front-panel { position: absolute; left: 0; top: 0; }
  .brand-block {
    position: absolute; left: 30px; top: 140px;
    display: flex; align-items: center; gap: 10px;
  }
  .brand-mark { width: 14px; height: 14px; background: var(--paper); flex: none; }
  .brand-name {
    color: var(--paper); font-weight: 700; font-size: 22px; line-height: 1.05;
    text-transform: uppercase; letter-spacing: 1px;
  }
  .company-title {
    position: absolute; left: 287px; top: 100px; width: 290px; text-align: center;
  }
  .company-title__main {
    color: var(--orange); font-weight: 700; font-size: 26px; letter-spacing: 0.5px;
    line-height: 1;
  }
  .company-title__sub {
    display: flex; align-items: center; gap: 12px; margin-top: 4px;
    color: var(--charcoal); font-weight: 500; font-size: 20px; letter-spacing: 3px;
  }
  .company-title__sub::before, .company-title__sub::after {
    content: ""; flex: 1; height: 2px; background: var(--rule);
  }
  .contact-name {
    position: absolute; left: 287px; top: 166px; width: 290px; text-align: center;
    color: var(--charcoal); font-weight: 700; font-size: 18px; letter-spacing: 2.5px;
    text-transform: uppercase;
  }
  .contact-line {
    position: absolute; left: 308px; display: flex; align-items: center; gap: 14px;
    color: var(--charcoal); font-weight: 700; letter-spacing: 1.5px;
  }
  .contact-line--phone { top: 208px; font-size: 17px; letter-spacing: 2.5px; }
  .contact-line--email { top: 252px; font-size: 15px; letter-spacing: 0.5px; }
  .contact-line--abn { top: 296px; font-size: 15px; letter-spacing: 1.5px; }
  .contact-line svg { flex: none; }
  .abn-label {
    width: 28px; text-align: center; font-size: 12px; letter-spacing: 0.5px;
  }

  /* back */
  .back-brand {
    position: absolute; left: 0; right: 0; top: 50px;
    display: flex; justify-content: center; align-items: center; gap: 14px;
  }
  .back-brand__mark { width: 26px; height: 26px; background: var(--orange); }
  .back-brand__name {
    color: var(--charcoal); font-weight: 700; font-size: 40px;
    text-transform: uppercase; letter-spacing: 2px;
  }
  .tagline {
    position: absolute; left: 0; right: 0; top: 136px; text-align: center;
    color: var(--charcoal); font-weight: 700; font-size: 20px; letter-spacing: 1.5px;
  }
  .service-band {
    position: absolute; left: 0; right: 0; bottom: 0; height: 182px;
    background: var(--orange);
    display: flex; flex-direction: column; justify-content: center; align-items: center;
    gap: 4px;
  }
  .service {
    display: flex; align-items: center; gap: 8px;
    color: var(--charcoal); font-weight: 700; font-size: 19px; letter-spacing: 1.5px;
    line-height: 1.25;
  }
  .service::before, .service::after {
    content: ""; width: 78px; height: 2px; background: var(--charcoal);
  }
</style>
</head>
<body>

<section class="card card--front" aria-label="Business card front">
  <svg class="front-panel" width="620" height="369" viewBox="0 0 620 369" aria-hidden="true">
    <polygon points="0,0 167,0 248,369 0,369" fill="var(--orange)"/>
  </svg>
  <div class="brand-block">
    <span class="brand-mark"></span>
    <span class="brand-name">Ashby<br>Paving<br>Works</span>
  </div>

  <div class="company-title">
    <div class="company-title__main">ASHBY PAVING</div>
    <div class="company-title__sub">WORKS</div>
  </div>

  <p class="contact-name">Mark Lowry</p>

  <div class="contact-line contact-line--phone">
    <svg width="28" height="28" viewBox="0 0 28 28" aria-hidden="true">
      <circle cx="14" cy="14" r="12" fill="none" stroke="var(--charcoal)" stroke-width="2.2"/>
      <path d="M10 8.5c-1 .6-1.6 1.7-1 3.4 1 2.8 3.6 5.6 6.6 7 1.6.7 2.8.1 3.4-.9l-2.3-2.2-1.6 1c-1.4-.7-2.9-2.3-3.6-3.7l1-1.6z" fill="var(--charcoal)"/>
    </svg>
    <span>0412885107</span>
  </div>

  <div class="contact-line contact-line--email">
    <svg width="28" height="26" viewBox="0 0 28 26" aria-hidden="true">
      <path d="M2 10 L14 2 L26 10 V24 H2 Z" fill="var(--charcoal)"/>
      <path d="M2 10 L14 18 L26 10" fill="none" stroke="#fff" stroke-width="1.6"/>
      <path d="M2 24 L11 16 M26 24 L17 16" stroke="#fff" stroke-width="1.4"/>
    </svg>
    <span>marklowry@pavemail.com.au</span>
  </div>

  <div class="contact-line contact-line--abn">
    <span class="abn-label">ABN</span>
    <span>27613048852</span>
  </div>
</section>

<section class="card card--back" aria-label="Business card back">
  <div class="back-brand">
    <span class="back-brand__mark"></span>
    <span class="back-brand__name">Ashby Paving Works</span>
  </div>
  <p class="tagline">For all your concreting solutions</p>
  <div class="service-band">
    <span class="service">Excavation</span>
    <span class="service">Exposed &amp; colour concrete</span>
    <span class="service">House &amp; shed slabs</span>
    <span class="service">Driveways</span>
    <span class="service">Landing &amp; steps</span>
  </div>
</section>

</body>
</html>
```